Company Values One-Pager

We're a recruitment firm based in Singapore, focused on the startup tech and VC sectors. www.dorvellagroup.com

As we're now at the point of growing and hiring, we want a one-pager (PDF or whatever) that summarises us and our company values.

I've attached a short PowerPoint that goes into the values etc.

Industry/Entity Type

It Company

Font styles to use
Sans Serif

Requirements
Must have
• We like a 'clean' look. Our logo is bright and simple, and that's what we're looking for.
• The official colour code for the logo is seafoam green
• www.huetrove.net/color/71EEB8/sea_foam_green
• Our website also gives a good insight.
• I'd like logos that summarise each value alongside them. i.e + for positivity, a letter for delivery etc. (Just ideas - please innovate!)
Should not have
• Nothing dark - just keep it simple and fresh

```html
<!DOCTYPE html>
<html lang="en">
<head>
<meta charset="utf-8">
<title>Dorvella Group – Who We Are</title>
<link href="https://fonts.googleapis.com/css2?family=Jost:wght@400;500;600&display=swap" rel="stylesheet">
<style>
  :root{
    --seafoam:#5fd9a0;
    --seafoam-text:#3fc98a;
    --ink:#3c3c3c;
    --ink-soft:#4a4a4a;
    --paper:#f1f1ef;
    --backdrop:#dfe5e4;
    --footer-dark:#4b4b4b;
    --photo-light:#d3eef7;
    --photo-mid:#8fd0ea;
  }
  *{box-sizing:border-box;margin:0;padding:0}
  html,body{width:1200px;height:960px;overflow:hidden}
  body{background:var(--backdrop);font-family:"Jost",sans-serif;color:var(--ink)}
  .flyer{position:absolute;left:275px;top:20px;width:650px;height:920px;background:var(--paper);overflow:hidden}
  .brand{position:absolute;top:60px;left:0;width:100%;text-align:center;font-size:30px;font-weight:500;letter-spacing:6px;color:var(--seafoam-text)}
  .hero-band{position:absolute;left:0;top:153px;width:420px;height:270px;background:var(--seafoam)}
  .hero-photo{position:absolute;left:18px;top:166px;width:386px;height:243px;background:radial-gradient(circle at 55% 50%,var(--photo-light),var(--photo-mid) 80%)}
  .tagline{position:absolute;left:420px;top:238px;width:215px;font-weight:400;text-transform:uppercase;line-height:1.1;color:var(--ink);white-space:nowrap}
  .tagline span{display:block}
  .t1{font-size:17px}.t2{font-size:22px}.t3{font-size:25px}.t4{font-size:22px}
  .col-title{font-size:23px;font-weight:600;text-transform:uppercase;letter-spacing:.5px;color:var(--ink)}
  .who{position:absolute;left:30px;top:464px;width:210px}
  .who dl{margin-top:20px}
  .who dt{font-size:13px;font-weight:600;text-transform:uppercase;margin-top:16px}
  .who dt:first-child{margin-top:0}
  .who dd{font-size:10.5px;line-height:1.3;color:var(--ink-soft)}
  .divider{position:absolute;left:250px;top:462px;width:1px;height:350px;background:#d3d3d3}
  .values{position:absolute;left:285px;top:468px;width:355px}
  .values .col-title{font-size:18px}
  .value{margin-top:20px}
  .value:first-of-type{margin-top:24px}
  .value-row{display:flex;align-items:center;gap:8px}
  .value-icon{flex:0 0 22px;width:22px;height:22px;border-radius:50%;background:var(--seafoam);display:flex;align-items:center;justify-content:center}
  .value-head{display:inline-flex;align-items:baseline;gap:7px;border-bottom:1px solid var(--seafoam);padding-bottom:1px;white-space:nowrap}
  .value-name{font-size:14px;text-transform:uppercase;color:var(--seafoam-text)}
  .value-def{font-size:10px;color:var(--ink)}
  .value p{font-size:10.5px;line-height:1.3;margin-top:10px;margin-left:30px;color:var(--ink-soft)}
  .footer-dark{position:absolute;left:230px;top:866px;width:420px;height:54px;background:var(--footer-dark)}
  .footer-green{position:absolute;left:0;top:843px;width:270px;height:77px}
  .phone-badge{position:absolute;left:122px;top:826px;width:34px;height:34px;border-radius:50%;background:var(--paper);display:flex;align-items:center;justify-content:center}
  .phone-number{position:absolute;left:30px;top:868px;font-size:29px;font-weight:600;color:#fff;letter-spacing:.5px}
  .contact{position:absolute;top:878px;font-size:10.5px;line-height:1.35;color:#fff;display:flex;gap:8px;align-items:flex-start}
  .contact.address{left:272px}
  .contact.web{left:480px}
  .contact-sep{position:absolute;left:466px;top:874px;width:1px;height:38px;background:#777}
</style>
</head>
<body>
<main class="flyer">
  <div class="brand">DORVELLA GROUP</div>

  <div class="hero-band"></div>
  <div class="hero-photo" role="img" aria-label="Photo of a businessman touching a glowing digital 'Core Values' search icon"></div>

  <h1 class="tagline">
    <span class="t1">Recruitment partner</span>
    <span class="t2">for the startup</span>
    <span class="t3">ecosystem in</span>
    <span class="t4">South-East Asia</span>
  </h1>

  <section class="who">
    <h2 class="col-title">Who we are</h2>
    <dl>
      <dt>What</dt>
      <dd>We are the ‘recruitment partner for the startup ecosystem in South-East Asia’; partnering with Venture Capital and startup tech firms, HQ’d out of Singapore.</dd>
      <dt>Who</dt>
      <dd>Established by Aran Teo &amp; Simon Harlow</dd>
      <dt>When</dt>
      <dd>Opened our doors in September 2016</dd>
      <dt>Longer-term goal</dt>
      <dd>Asia and Global expansion</dd>
      <dt>Core values</dt>
      <dd>Positivity - Proactivity - Teamwork - Delivery</dd>
    </dl>
  </section>

  <div class="divider"></div>

  <section class="values">
    <h2 class="col-title">Our core values</h2>
    <div class="value">
      <div class="value-row">
        <span class="value-icon"><svg width="12" height="12" viewBox="0 0 12 12" aria-hidden="true"><path d="M6 1v10M1 6h10" stroke="#fff" stroke-width="2.2" stroke-linecap="round"/></svg></span>
        <div class="value-head"><span class="value-name">Positivity</span><span class="value-def">the character of being positive</span></div>
      </div>
      <p>We look on the bright side…<br>and don’t let limiting beliefs hold us back</p>
    </div>
    <div class="value">
      <div class="value-row">
        <span class="value-icon"><svg width="12" height="12" viewBox="0 0 12 12" aria-hidden="true"><path d="M1 6h9M6.5 2.5L10 6l-3.5 3.5" stroke="#fff" stroke-width="2" fill="none" stroke-linecap="round" stroke-linejoin="round"/></svg></span>
        <div class="value-head"><span class="value-name">Proactivity</span><span class="value-def">to initiate change rather than reacting to events</span></div>
      </div>
      <p>We don’t wait… we make things happen</p>
    </div>
    <div class="value">
      <div class="value-row">
        <span class="value-icon"><svg width="14" height="12" viewBox="0 0 14 12" aria-hidden="true"><circle cx="4.5" cy="6" r="3.3" stroke="#fff" stroke-width="1.6" fill="none"/><circle cx="9.5" cy="6" r="3.3" stroke="#fff" stroke-width="1.6" fill="none"/></svg></span>
        <div class="value-head"><span class="value-name">Teamwork</span><span class="value-def">working together</span></div>
      </div>
      <p>We work together… to solve problems,<br>find solutions, and celebrate the good times</p>
    </div>
    <div class="value">
      <div class="value-row">
        <span class="value-icon"><svg width="12" height="12" viewBox="0 0 12 12" aria-hidden="true"><path d="M1.5 6.5l3 3 6-7" stroke="#fff" stroke-width="2" fill="none" stroke-linecap="round" stroke-linejoin="round"/></svg></span>
        <div class="value-head"><span class="value-name">Delivery</span><span class="value-def">to achieve what is desired, expected or promised</span></div>
      </div>
      <p>We do what we say we’re going to do…<br>for our candidates, clients, and colleagues alike</p>
    </div>
  </section>

  <div class="footer-dark"></div>
  <svg class="footer-green" viewBox="0 0 270 77" aria-hidden="true"><polygon points="0,0 245,0 270,77 0,77" fill="var(--seafoam)"/></svg>
  <div class="phone-badge">
    <svg width="18" height="18" viewBox="0 0 24 24" aria-hidden="true"><path d="M3 9c0-3 4-5 9-5s9 2 9 5v2h-5V9c-1-1-7-1-8 0v2H3z M7 12h10l2 8H5z" fill="#9a9a9a"/></svg>
  </div>
  <div class="phone-number">+65 3040 2868</div>

  <div class="contact address">
    <svg width="9" height="12" viewBox="0 0 10 14" aria-hidden="true"><path d="M5 0a5 5 0 0 1 5 5c0 4-5 9-5 9S0 9 0 5a5 5 0 0 1 5-5z" fill="var(--seafoam)"/><circle cx="5" cy="5" r="2" fill="var(--footer-dark)"/></svg>
    <span>48 Merrow Street, The Quadrant,<br>#05-02, Singapore 068210</span>
  </div>
  <div class="contact-sep"></div>
  <div class="contact web">
    <svg width="10" height="28" viewBox="0 0 10 28" aria-hidden="true"><rect x="0" y="2" width="10" height="7" fill="var(--seafoam)"/><path d="M0 2l5 4 5-4" stroke="var(--footer-dark)" fill="none"/><circle cx="5" cy="21" r="4.5" fill="var(--seafoam)"/></svg>
    <span>info@dorvellagroup.com<br>www.dorvellagroup.com</span>
  </div>
</main>
</body>
</html>
```